Vexlink Website

We need a website for a new Telecommunications company based in Australia. Our service is offered to people who are in the middle of moving properties as our major channel partners relocate renters and home owners. The website will outline the products we sell, which will include pricing as well as provide information for people who are in the middle of a move. Our client base will not come from any demographic, however 95% will be people renting properties and therefore most likely range in age from 18 and upwards. I would like to have an energetic feel to the website with a young theme. It needs full integration with Social Media, must be mobile centric as well, must include video as well as have chat options for visitors and be as interactive as possible . It should not be too cluttered as it needs to be clean and feel fresh. People who are moving are time poor and stressed (I am sure you have all moved!) and therefore our service needs to be complimentary and simple for them to engage with. We have a channel passing hot leads for this purpose, however we would like to market our services to others outside of this channel. We are offering most services such as home phone, internet and prepaid mobiles as unlimited services to make things simple and easy to commit to. Logo at this stage is Red, however we also need soothing colours on the site. I like the website layout of Plumvane.com as an example, as it is clean and delivers the type of feel we are after. Your design does not have to mimic it, it just needs to give off the same feel.
Updates

Specific Competitors websites include the following:

http://www.brisquell.com.au/
http://www.talvorin.com.au/index.asp
http://gormesta.com.au/
http://www.kelbrantix.com.au/

Our site needs to be far more interactive than these.  Chat prompts once someone is on the site would be useful - asking "Are you ready to move?" "Do you want everything unlimited?" - click to chat, etc.

Hi Designers,

Could you please look at making the designs more Telecommunications focused.  Our primary focus is to move peoples phone services, so the Telco component and Broadband and internet is a key component.  The moving information is good, however none of the designs addresses the Telecommunications part, I want it clear that when someone comes to the site they can get a new fixed line, internet and pre paid mobile phone plan.

Thanks

Ned

Target Market(s)

People moving property who want to get their telecommunication and internet services connected at their new place.

Industry/Entity Type

Internet

Requirements
Must have
• Social Media
Video section
How to section
Pricing section
Moving information section
Useful links section
Live chat

```html
<!DOCTYPE html>
<html lang="en">
<head>
<meta charset="utf-8">
<title>Vexlink – Get Connected While You Are Moving House</title>
<link href="https://fonts.googleapis.com/css2?family=Arimo:ital,wght@0,400;0,700;1,400;1,700&display=swap" rel="stylesheet">
<style>
:root{
  --red:#e3262b;
  --red-dark:#b5161b;
  --red-soft:#f25a5e;
  --ink:#333333;
  --ink-soft:#555555;
  --grey-band:#dcdcdc;
  --grey-light:#f2f2f2;
  --grey-line:#cfcfcf;
  --charcoal:#3a3a3a;
  --black:#000000;
  --white:#ffffff;
  --orange:#e8661c;
}
*{box-sizing:border-box;margin:0;padding:0}
html,body{width:1120px;height:1200px;overflow:hidden;background:var(--white)}
body{font-family:"Arimo",Arial,sans-serif;color:var(--ink);position:relative}
.abs{position:absolute}

/* header */
.site-header{left:0;top:0;width:1120px;height:125px;background:linear-gradient(#ffffff 0,#ffffff 60px,#ececec 125px)}
.brand{left:208px;top:16px;display:flex;align-items:center;gap:10px}
.brand-dot{width:34px;height:34px;border-radius:50%;background:var(--red)}
.brand-name{font-size:26px;font-weight:700;color:var(--red)}
.brand-url{left:208px;top:56px;font-size:9px;color:var(--ink-soft)}
.social-top{left:810px;top:20px;display:flex;gap:4px}
.social-top span{width:18px;height:18px;border-radius:3px;display:block}
.search{left:795px;top:51px;display:flex;gap:10px}
.search-input{width:118px;height:20px;border:1px solid var(--grey-line);font-size:10px;padding:3px 5px;color:var(--ink)}
.search-go{width:24px;height:20px;background:var(--red);color:var(--white);font-size:10px;text-align:center;line-height:20px}
.main-nav{left:150px;top:90px;width:820px;height:35px;display:flex;border:1px solid var(--grey-line);background:linear-gradient(#ffffff,#f1f1f1)}
.main-nav a{flex:1;text-align:center;line-height:33px;font-size:12px;color:var(--ink);text-decoration:none;border-right:1px solid var(--grey-line)}
.main-nav a:last-child{border-right:0}

/* hero */
.hero{left:150px;top:140px;width:820px;height:330px;border:1px solid var(--grey-line);box-shadow:0 10px 14px -8px rgba(0,0,0,.45);background:#c9c9c9}
.hero-photo{left:0;top:0;width:440px;height:255px;background:linear-gradient(90deg,#8a8f96 0,#c9d3de 35%,#e9e6e1 55%,#c8a77a 100%)}
.hero-caption{left:0;top:205px;width:440px;height:50px;background:rgba(60,60,60,.7);color:var(--white);font-size:14px;font-weight:700;padding:8px 18px;line-height:17px}
.hero-band{left:0;top:255px;width:440px;height:75px;background:linear-gradient(#9a9a9a,#6e6e6e);text-align:center;color:var(--white);font-weight:700}
.hero-title{font-size:36px;line-height:40px;padding-top:5px}
.hero-sub{font-size:21px;line-height:24px}
.hero-sub em{font-style:normal;color:var(--red)}
.dots{left:392px;top:263px;display:flex;gap:3px}
.dots span{width:8px;height:8px;border-radius:50%;background:#cccccc}
.dots span:first-child{background:var(--orange)}
.video-panel{left:440px;top:0;width:380px;height:330px;background:linear-gradient(#e1e1e1,#c4c4c4)}
.video-title{left:12px;top:4px;font-size:18px;font-weight:700;color:#444}
.video-screen{left:10px;top:25px;width:360px;height:270px;background:var(--black)}
.video-controls{left:10px;top:295px;width:360px;height:22px;background:linear-gradient(#6b6b6b,#3a3a3a)}

/* quote */
.quote-band{left:0;top:492px;width:1120px;height:135px;background:var(--grey-band)}
.quote-text{left:176px;top:20px;font-size:26px;font-weight:700;font-style:italic;color:#555;line-height:33px}
.quote-by{left:705px;top:95px;font-size:14px;color:var(--ink-soft)}
.quote-by b{color:var(--orange);font-weight:400}

/* feature cards */
.card{top:645px;height:192px;border:1px solid var(--grey-line);border-radius:4px;background:var(--white);box-shadow:0 1px 3px rgba(0,0,0,.12)}
.card-title{height:28px;line-height:28px;padding-left:14px;font-size:14px;font-weight:700;color:#444;border-bottom:2px solid var(--red);margin:0 0 0 0}
.card-icon{left:10px;top:47px;width:58px;height:58px}
.card-text{left:92px;top:43px;width:150px;font-size:11px;line-height:15px;color:var(--ink-soft)}
.card-more{top:160px;width:70px;height:20px;border:1px solid var(--grey-line);border-radius:10px;font-size:10px;text-align:center;line-height:18px;background:linear-gradient(#ffffff,#e8e8e8);color:#444}

/* price finder */
.finder{left:150px;top:850px;width:402px;height:122px;background:linear-gradient(var(--red-soft),var(--red-dark));border-radius:4px}
.finder-tab{left:20px;top:6px;width:140px;height:22px;background:var(--charcoal);color:var(--white);font-size:10px;line-height:22px;padding-left:12px;border-radius:3px 3px 0 0}
.finder-body{left:8px;top:28px;width:386px;height:84px;border:1px solid rgba(255,255,255,.5);border-radius:4px}
.finder-label{font-size:12px;font-weight:700;color:var(--white)}
.field{height:20px;background:var(--white);border-radius:3px;font-size:10px;line-height:20px;color:#444;overflow:hidden;display:flex}
.field b{background:var(--charcoal);color:var(--white);font-weight:400;padding:0 8px}
.finder-search{height:20px;background:var(--red);border:1px solid #ffffff80;border-radius:3px;color:var(--white);font-size:11px;font-weight:700;line-height:18px;display:flex}
.finder-search i{width:20px;background:var(--charcoal);font-style:normal;text-align:center;font-size:8px}

/* live chat */
.chat{left:570px;top:850px;width:400px;height:122px;background:linear-gradient(var(--red-soft),var(--red-dark));border-radius:4px;overflow:hidden}
.chat-head{left:0;top:0;width:400px;height:26px;background:linear-gradient(#555,#2f2f2f);color:var(--white);font-size:15px;line-height:26px;padding-left:92px}
.chat-photo{left:14px;top:4px;width:70px;height:118px;background:linear-gradient(#d8b9a2,#2d2d2d)}
.chat-q{left:95px;top:32px;font-size:19px;font-weight:700;font-style:italic;color:var(--white)}
.chat-call{left:140px;top:57px;font-size:14px;color:var(--white)}
.chat-phone{left:135px;top:80px;font-size:25px;font-weight:700;color:var(--white)}

/* footer */
.footer{left:0;top:987px;width:1120px;height:191px;background:var(--grey-band)}
.footer-frame{left:150px;top:8px;width:820px;height:178px;border:3px solid var(--charcoal)}
.footer-col h4{font-size:13px;font-weight:700;color:#444;margin-bottom:8px}
.footer-col li{list-style:none;font-size:11px;line-height:13.5px;color:var(--ink-soft)}
.follow li{display:flex;align-items:center;gap:8px;line-height:25px}
.follow li span{width:20px;height:20px;border-radius:3px;display:block}
.newsletter{left:512px;top:20px;width:255px;height:120px;border:1px solid var(--grey-line);border-radius:4px;background:var(--grey-band)}
.newsletter-head{height:28px;background:linear-gradient(#555,#2f2f2f);color:var(--white);font-size:14px;line-height:28px;padding-left:20px;border-radius:4px 4px 0 0}
.newsletter-title{left:20px;top:40px;font-size:14px;color:#444}
.newsletter-sub{left:22px;top:58px;font-size:9px;color:var(--ink-soft)}
.newsletter-form{left:18px;top:80px;display:flex}
.newsletter-form span{width:160px;height:22px;background:var(--white);font-size:9px;line-height:22px;padding-left:8px;color:#444;border-radius:3px 0 0 3px}
.newsletter-form b{width:60px;height:22px;background:var(--charcoal);color:var(--white);font-size:10px;line-height:22px;text-align:center;border-radius:0 3px 3px 0}
.copyright{left:0;top:1178px;width:1120px;height:22px;background:#2b2b2b;color:var(--white);font-size:10px;text-align:center;line-height:22px}
</style>
</head>
<body>

<header class="site-header abs">
  <div class="brand abs"><span class="brand-dot"></span><span class="brand-name">Vexlink</span></div>
  <div class="brand-url abs">www.vexlink.com.au</div>
  <div class="social-top abs">
    <span style="background:#3b5a98"></span><span style="background:#39a9dd"></span><span style="background:#1c6fa6"></span><span style="background:#f28a1e"></span>
  </div>
  <div class="search abs"><div class="search-input">Site search...</div><div class="search-go">Go</div></div>
  <nav class="main-nav abs">
    <a href="#" style="flex:0 0 154px">Home</a>
    <a href="#" style="flex:0 0 194px">What We Connect</a>
    <a href="#" style="flex:0 0 145px">About Us</a>
    <a href="#" style="flex:0 0 144px">Partners</a>
    <a href="#">Contact Us</a>
  </nav>
</header>

<section class="hero abs">
  <div class="hero-photo abs" role="img" aria-label="Businesswoman on the phone beside a city tower, next to a stack of moving boxes"></div>
  <div class="hero-caption abs">We will connect your utilities, wherever<br>you move. Save your time and money.</div>
  <div class="hero-band abs">
    <div class="hero-title">Get Connected</div>
    <div class="hero-sub">While You Are <em>Moving House</em></div>
  </div>
  <div class="dots abs"><span></span><span></span><span></span></div>
  <div class="video-panel abs">
    <div class="video-title abs">See How It Works</div>
    <div class="video-screen abs">
      <svg width="360" height="270"><circle cx="180" cy="135" r="6" fill="none" stroke="#777" stroke-width="3" stroke-dasharray="3 2"/></svg>
    </div>
    <div class="video-controls abs">
      <svg width="360" height="22">
        <rect x="6" y="6" width="3" height="10" fill="#ddd"/><rect x="11" y="6" width="3" height="10" fill="#ddd"/>
        <rect x="22" y="6" width="2" height="10" fill="#ddd"/><polygon points="32,6 25,11 32,16" fill="#ddd"/>
        <rect x="44" y="10" width="125" height="3" rx="1.5" fill="#999"/><circle cx="46" cy="11" r="5" fill="#ccc"/>
        <rect x="175" y="5" width="46" height="12" fill="#111"/>
        <text x="178" y="14" font-size="8" fill="#ccc" font-family="Arimo,sans-serif">00:00 / <tspan fill="#e3262b">01:47</tspan></text>
        <rect x="240" y="10" width="40" height="3" fill="#ccc"/><rect x="272" y="6" width="4" height="10" fill="#eee"/>
        <polygon points="284,9 288,9 292,5 292,17 288,13 284,13" fill="#ddd"/>
        <rect x="315" y="6" width="14" height="10" fill="#888"/><rect x="335" y="6" width="16" height="10" fill="#888"/>
      </svg>
    </div>
  </div>
</section>

<section class="quote-band abs">
  <p class="quote-text abs">“Lorem ipsum dolor sit amet, consecteteur adipiscing elit.<br>Set diem nonumy in convalis gravida neque...”</p>
  <p class="quote-by abs"><b>John Doe,</b> London</p>
</section>

<article class="card abs" style="left:150px;width:254px">
  <h3 class="card-title">Moving House?</h3>
  <svg class="card-icon abs" viewBox="0 0 58 58" aria-hidden="true">
    <polygon points="29,6 6,28 16,28 16,34 42,34 42,28 52,28" fill="#e3262b"/>
    <rect x="22" y="36" width="14" height="6" fill="#e3262b"/>
    <polygon points="16,44 42,44 42,50 16,50" fill="#e3262b"/>
    <polygon points="24,22 29,16 34,22" fill="#fff"/>
  </svg>
  <p class="card-text abs">Lorem ipsum dolor sit amet, consecteteur adipis cing elit. set diem nonumy in convalis gravida neque. Nulla gravida neque vesti bulum metis a acumsan, aliquam in sagittis ut.</p>
  <div class="card-more abs" style="left:92px">Read more</div>
</article>

<article class="card abs" style="left:429px;width:261px">
  <h3 class="card-title">Get Connected</h3>
  <svg class="card-icon abs" viewBox="0 0 58 58" aria-hidden="true">
    <rect x="8" y="8" width="42" height="42" rx="6" fill="none" stroke="#e3262b" stroke-width="4"/>
    <rect x="14" y="17" width="14" height="24" rx="7" transform="rotate(-40 21 29)" fill="none" stroke="#333" stroke-width="3"/>
    <rect x="30" y="17" width="14" height="24" rx="7" transform="rotate(-40 37 29)" fill="none" stroke="#333" stroke-width="3"/>
  </svg>
  <p class="card-text abs">Lorem ipsum dolor sit amet, consecteteur adipis cing elit. set diem nonumy in convalis gravida neque. Nulla gravida neque vesti bulum metis a acumsan, aliquam in sagittis ut.</p>
  <div class="card-more abs" style="left:92px">Read more</div>
</article>

<article class="card abs" style="left:708px;width:261px">
  <h3 class="card-title">How It works</h3>
  <div class="card-icon abs" role="img" aria-label="Icon of a worker digging beside a red question mark" style="background:linear-gradient(#555,#333);border-radius:4px;opacity:.85"></div>
  <p class="card-text abs">Lorem ipsum dolor sit amet, consecteteur adipis cing elit. set diem nonumy in convalis gravida neque. Nulla gravida neque vesti bulum metis a acumsan, aliquam in sagittis ut.</p>
  <div class="card-more abs" style="left:95px">Read more</div>
</article>

<section class="finder abs">
  <div class="finder-tab abs">Vexlink Price FINDER</div>
  <div class="finder-body abs">
    <span class="finder-label abs" style="left:38px;top:15px">Price</span>
    <span class="finder-label abs" style="left:38px;top:40px">City</span>
    <div class="field abs" style="left:103px;top:12px;width:125px"><b>Minimum</b></div>
    <div class="field abs" style="left:238px;top:12px;width:125px"><b>Maximum</b></div>
    <div class="field abs" style="left:103px;top:38px;width:125px;padding-left:6px;justify-content:space-between">Melbourne<b style="padding:0 5px">▾</b></div>
    <div class="finder-search abs" style="left:238px;top:38px;width:125px"><i>▶</i><span style="flex:1;text-align:center">SEARCH</span></div>
  </div>
</section>

<section class="chat abs">
  <div class="chat-head abs">LIVE CHAT</div>
  <div class="chat-photo abs" role="img" aria-label="Support agent wearing a headset"></div>
  <div class="chat-q abs">Have a question?</div>
  <div class="chat-call abs">Call Us with our Staff&nbsp; :</div>
  <div class="chat-phone abs">(888) - XXX - XXXX</div>
</section>

<footer class="footer abs">
  <div class="footer-frame abs">
    <div class="footer-col abs" style="left:21px;top:12px">
      <h4>Main menu</h4>
      <ul><li>Home</li><li>What We Connect</li><li>About Us</li><li>Partners</li><li>How It Works</li><li>Latest News &amp; Events</li><li>Newsletter</li><li>Testimonials</li><li>Contact Us</li></ul>
    </div>
    <div class="footer-col abs" style="left:156px;top:12px">
      <h4>Useful Links</h4>
      <ul><li>Lorem ipsum</li><li>Lorem ipsum dolor</li><li>Lorem ipsum</li><li>Lorem ipsum</li><li>Lorem ipsum</li><li>Lorem ipsum dolor</li><li>Lorem ipsum dolor sit amet</li><li>Lorem ipsum dolor sit amet</li><li>Lorem ipsum</li></ul>
    </div>
    <div class="footer-col follow abs" style="left:377px;top:12px">
      <h4>Follow Us</h4>
      <ul>
        <li><span style="background:#3b5a98"></span>Friendlane</li>
        <li><span style="background:#39a9dd"></span>Chirpline</li>
        <li><span style="background:#1c6fa6"></span>Worknet</li>
        <li><span style="background:#f28a1e"></span>RSS</li>
      </ul>
    </div>
    <div class="newsletter abs">
      <div class="newsletter-head">Newsletter</div>
      <div class="newsletter-title abs">SIGN UP for Our Newsletter</div>
      <div class="newsletter-sub abs">and start receiving our new look monthly</div>
      <div class="newsletter-form abs"><span>Your email address</span><b>SUBMIT</b></div>
    </div>
  </div>
</footer>
<div class="copyright abs">Copyright &copy; 2012, Vexlink.com.au. All rights reserved.</div>

</body>
</html>
```